I’d like to see something with similar colors and design concept to the “Your Wallet Knows the Way” book included in attchment

Create a book cover with front cover, and full front, spine and back cover spread.
Simple and clean design. See design inspiration below.
Size 6X9
Title of the book: Find Your Shelf! Veteran Editors Reveal Quiet Methods

Please leave space for 6 authors names on the front cover. Authors names will be provided at a later time.

Back of book should included the name of the publishing company:
Lantern Grove Publishing

As well as the following synopsis
The landscape of the publishing industry is changing. Gone are the days of coveted gatekeepers controlling content and dictating the messages being distributed. With the rise of technology, social media , self-publishing platforms, and independent bookstores, there are increased opportunities for people to share their ideas, messages, and stories with the world through books. The types of books that we’re publishing are also evolving — mini-books, audio books, journals, multi-author books, cook books, children’s books, comic books, coloring books, interactive books, tarot and oracle card decks are all expanding the podium for people to express ideas and influence the culture. More and more entrepreneurs are posturing themselves as thought leaders by leveraging this growing platform.
But that doesn't mean it’s easy.
Even with the expanding platforms and opportunities, only a fraction of people with publishing ambitions are able to achieve this coveted dream held by so many. It can be a daunting process for budding authors trying to maneuver through the writing, packaging, marketing, and publishing processes alone.

In this book you'll find passionate, purpose-driven, and well-versed experts working in the various areas of publishing, eager to help open your eyes to the promise of publishing and effortlessly guide you through the process.

Colors
0094D4
00A9DD
6FCCEA
C7EBF8
E9F6FB
FFF300
FFF600
FEFA6F
FFFEC7
FFFEE8
FFC000
F8CF3A
FAE287
FDF2CF
FEFAEE
F0912C
F2A743
F7CA91
FBE8D2
FDF5EE
EE7325
F08F49
F5BC92
FAE3D3
FDF4ED
6B429C
8869AF
B7A5CE
E3DAEB
F3F0F8

```html
<!DOCTYPE html>
<html lang="en">
<head>
<meta charset="utf-8">
<title>Find Your Shelf! – Cover Spread</title>
<link rel="stylesheet" href="https://fonts.googleapis.com/css2?family=Dosis:wght@300;400;500;600&family=Didact+Gothic&display=swap">
<style>
  :root {
    --stage: #333333;
    --sheet: #ffffff;
    --sage: #a3b1a5;
    --maroon: #8c4c45;
    --ink: #3b1209;
    --cream: #f4e6de;
    --dot: #8a1c14;
    --display: "Dosis", sans-serif;
    --body: "Didact Gothic", sans-serif;
  }
  * { box-sizing: border-box; margin: 0; padding: 0; }
  html, body { width: 1200px; height: 1177px; overflow: hidden; background: var(--stage); }
  .canvas { position: relative; width: 1200px; height: 1177px; }
  .sheet { position: absolute; left: 118px; top: 230px; width: 982px; height: 680px; background: var(--sheet); }

  /* Back cover */
  .back { position: absolute; left: 138px; top: 250px; width: 415px; height: 640px; background: var(--cream); }
  .back-head { position: absolute; left: 0; top: 0; width: 415px; height: 224px; background: var(--sage); }
  .back-head .accent { position: absolute; right: 0; top: 0; width: 105px; height: 224px; background: var(--maroon); }
  .back-head .word-big {
    position: absolute; left: 26px; top: 9px; font-family: var(--display); font-weight: 500;
    font-size: 110px; line-height: 1; letter-spacing: 16px; color: var(--maroon); white-space: nowrap;
  }
  .back-head .word-bold {
    position: absolute; left: 22px; top: 140px; font-family: var(--display); font-weight: 600;
    font-size: 56px; line-height: 1; color: var(--ink); letter-spacing: 0.5px; white-space: nowrap;
  }
  .back-band {
    position: absolute; left: 0; top: 224px; width: 415px; height: 50px; background: var(--maroon);
    color: #fff; font-family: var(--display); font-weight: 400; font-size: 22px;
    display: flex; align-items: center; justify-content: center; letter-spacing: 0.5px; white-space: nowrap;
  }
  .synopsis {
    position: absolute; left: 30px; top: 314px; width: 356px;
    font-family: var(--body); font-size: 9.6px; line-height: 1.4; color: #2a2a2a; text-align: justify;
  }
  .synopsis p + p { margin-top: 11px; }
  .synopsis .lead { color: #000; font-size: 10px; }
  .back-publisher {
    position: absolute; left: 30px; top: 611px; font-family: var(--body); font-size: 11px; color: var(--dot);
  }

  /* Spine */
  .spine { position: absolute; left: 572px; top: 250px; width: 75px; height: 640px; background: var(--sage); }
  .spine-head {
    position: absolute; left: 0; top: 0; width: 75px; height: 274px; background: var(--ink);
    display: flex; justify-content: center; padding-top: 22px;
  }
  .spine-title {
    writing-mode: vertical-rl; font-family: var(--display); font-weight: 500; color: #fff;
    font-size: 32px; letter-spacing: 1px; line-height: 1;
  }
  .spine-subtitle {
    position: absolute; left: 0; top: 295px; width: 75px; display: flex; justify-content: center;
    writing-mode: vertical-rl; font-family: var(--display); font-weight: 500; color: var(--dot);
    font-size: 16px; line-height: 75px; letter-spacing: 0.5px;
  }
  .spine-publisher {
    position: absolute; left: 0; bottom: 10px; width: 75px; text-align: center;
    font-family: var(--body); font-weight: 700; font-size: 10px; line-height: 1.2; color: var(--dot);
  }

  /* Front cover */
  .front { position: absolute; left: 666px; top: 250px; width: 418px; height: 640px; background: var(--sage); }
  .front .word-big {
    position: absolute; left: 0; top: 10px; width: 418px; text-align: center; padding-left: 30px;
    font-family: var(--display); font-weight: 500; font-size: 150px; line-height: 1;
    letter-spacing: 30px; color: var(--maroon); white-space: nowrap;
  }
  .front .word-bold {
    position: absolute; left: 0; top: 208px; width: 418px; text-align: center;
    font-family: var(--display); font-weight: 600; font-size: 74px; line-height: 1; color: var(--ink);
    white-space: nowrap;
  }
  .front .subtitle-box {
    position: absolute; left: 38px; top: 303px; width: 347px; height: 102px; background: var(--cream);
    display: flex; align-items: center; justify-content: center; text-align: center;
    font-family: var(--display); font-weight: 300; font-size: 35px; line-height: 1.08; color: var(--maroon);
  }
  .front .word-spaced {
    position: absolute; left: 0; top: 414px; width: 418px; text-align: center; padding-left: 16px;
    font-family: var(--display); font-weight: 500; font-size: 74px; line-height: 1;
    letter-spacing: 16px; color: var(--ink); white-space: nowrap;
  }
  .authors {
    position: absolute; left: 0; top: 508px; width: 418px; height: 132px; background: var(--maroon);
    padding-top: 20px; font-family: var(--display); font-weight: 400; font-size: 19px; line-height: 27px;
    color: var(--ink); text-align: center;
  }
  .authors .dot { color: var(--dot); font-size: 14px; margin: 0 4px; }
  .front-publisher {
    position: absolute; left: 110px; top: 619px; width: 208px; height: 21px; background: #fff;
    display: flex; align-items: center; justify-content: center;
    font-family: var(--body); font-size: 13.5px; color: #222;
  }
</style>
</head>
<body>
<main class="canvas">
  <div class="sheet"></div>

  <section class="back" aria-label="Back cover">
    <div class="back-head">
      <div class="accent"></div>
      <div class="word-big">FIND</div>
      <div class="word-bold">YOUR SHELF</div>
    </div>
    <div class="back-band">VETERAN EDITORS REVEAL QUIET METHODS</div>
    <div class="synopsis">
      <p>The landscape of the publishing industry is changing. Gone are the days of coveted gatekeepers controlling content and dictating the messages being distributed. With the rise of technology, social media , self-publishing platforms, and independent bookstores, there are increased opportunities for people to share their ideas, messages, and stories with the world through books. The types of books that we’re publishing are also evolving — mini-books, audio books, journals, multi-author books, cook books, children’s books, comic books, coloring books, interactive books, tarot and oracle card decks are all expanding the podium for people to express ideas and influence the culture. More and more entrepreneurs are posturing themselves as thought leaders by leveraging this growing platform.</p>
      <p>But that doesn't mean it’s easy.<br>Even with the expanding platforms and opportunities, only a fraction of people with publishing ambitions are able to achieve this coveted dream held by so many. It can be a daunting process for budding authors trying to maneuver through the writing, packaging, marketing, and publishing processes alone.</p>
      <p class="lead">In this book you'll find passionate, purpose-driven, and well-versed experts working in the various areas of publishing, eager to help open your eyes to the promise of publishing and effortlessly guide you through the process.</p>
    </div>
    <div class="back-publisher">Lantern Grove Publishing</div>
  </section>

  <section class="spine" aria-label="Spine">
    <div class="spine-head"><span class="spine-title">FIND YOUR SHELF</span></div>
    <div class="spine-subtitle">VETERAN EDITORS REVEAL QUIET METHODS</div>
    <div class="spine-publisher">Lantern<br>Grove<br>Publishing</div>
  </section>

  <section class="front" aria-label="Front cover">
    <div class="word-big">FIND</div>
    <div class="word-bold">YOUR SHELF</div>
    <div class="subtitle-box">VETERAN EDITORS<br>REVEAL QUIET</div>
    <div class="word-spaced">METHODS</div>
    <div class="authors">
      AUTHOR NAME 1<span class="dot">●</span>AUTHOR NAME 2<span class="dot">●</span><br>
      AUTHOR NAME 3<span class="dot">●</span>AUTHOR NAME 4<span class="dot">●</span><br>
      AUTHOR NAME 5<span class="dot">●</span>AUTHOR NAME 6<span class="dot">●</span>
    </div>
    <div class="front-publisher">Lantern Grove Publishing</div>
  </section>
</main>
</body>
</html>
```